We are the world's leading center for transgender surgery and have multiple locations.

We want a unique and dynamic business card that wows potential patients and referral sources (physicians, previous patients, etc). We are open to inventive designs, card shape, additional design on the back of the card, etc.

We are a surgical practice in a competitive environment and want to stand out as the leader in transgender surgery. We have multiple surgeons with unique talents who are impeccably trained with extensive experience. We are dedicated to our patients and their needs. We want the card to stand out and impress them. We want it to be suitable to all of the surgeons as well as our staff.

Our practice started as a small practice in San Francisco, CA and now has an additional location in Austin Texas (as well as another city to be announced later). Our practice has plastic surgeons, reconstructive urologists, general surgeons and gynecologists.

We continue to boast some of the lowest published phalloplasty complication rates in the world and our San Francisco microsurgeons that we have been working with for more than a year and a half have 0 microvascular take backs and 0 flap failures. Between our two centers in San Francisco, California and Austin, Texas, we perform 5-6 phalloplasties per week, making us one of the largest volume centers in the world.

Target Market(s)

Potential Transgender patients (all genders) and referring physicians

Industry/Entity Type

Surgeon

Contact Information for Business Card

Here is an example of one of our physicians:

Daniel R. Venko, MD
Reconstructive Urology for the Transgender Community
Diplomate, National Council of Renal Medicine with subspecialty certification in FPS and Reconstructive Surgery

812 Orchard Vale Rd
Suite 4
Fernmoor, CA 94917

phone 415-738-2914
fax 415-592-8167

Font styles to use
Sans Serif

Requirements
Must have
• Must have a unique look, but tasteful.
Nice to have
• ?
Should not have
• ?

```html
<!DOCTYPE html>
<html lang="en">
<head>
<meta charset="utf-8">
<title>Halden Center – Business Card</title>
<link rel="stylesheet" href="https://fonts.googleapis.com/css2?family=Lato:wght@400;700;900&display=swap">
<style>
  :root {
    --navy: #243570;
    --magenta: #a11f68;
    --card: #ffffff;
    --backdrop: #d6d6d8;
  }
  * { box-sizing: border-box; margin: 0; padding: 0; }
  html, body {
    width: 1200px; height: 1200px; overflow: hidden;
    background: var(--backdrop);
    font-family: "Lato", Arial, sans-serif;
  }
  .canvas { position: relative; width: 1200px; height: 1200px; }
  .card {
    position: absolute; background: var(--card);
    border-radius: 28px;
  }
  .card--front { left: 172px; top: 94px; width: 846px; height: 483px; }
  .card--back  { left: 170px; top: 612px; width: 848px; height: 484px; }

  .brand { position: absolute; display: flex; align-items: center; }
  .brand__dot { border-radius: 50%; background: var(--navy); flex: none; }
  .brand__text { color: var(--navy); font-weight: 900; line-height: 1; }
  .brand__name { display: block; letter-spacing: -0.5px; }
  .brand__tag { display: block; text-align: right; text-transform: uppercase; }

  .card--front .brand { left: 28px; top: 30px; }
  .card--front .brand__dot { width: 155px; height: 155px; margin-right: 12px; }
  .card--front .brand__name { font-size: 44px; }
  .card--front .brand__tag { font-size: 10px; margin-top: 5px; }

  .card--back .brand { left: 58px; top: 130px; }
  .card--back .brand__dot { width: 222px; height: 222px; margin-right: 14px; }
  .card--back .brand__name { font-size: 62px; }
  .card--back .brand__tag { font-size: 16px; margin-top: 6px; }

  .edge-tab {
    position: absolute; right: 0; top: 188px;
    width: 8px; height: 28px; border-radius: 4px 0 0 4px;
    background: var(--magenta);
  }

  .doctor { position: absolute; right: 32px; top: 180px; text-align: right; }
  .doctor__name { color: var(--navy); font-weight: 700; font-size: 38px; line-height: 46px; }
  .doctor__credentials { color: var(--magenta); font-size: 27px; line-height: 34px; }

  .address {
    position: absolute; right: 32px; top: 356px; text-align: right;
    color: var(--navy); font-size: 27px; line-height: 34px; font-style: normal;
  }
  .contact {
    position: absolute; left: 28px; top: 385px;
    color: var(--navy); font-size: 27px; line-height: 38px; list-style: none;
  }
  .contact li { display: flex; align-items: center; }
  .contact svg { width: 22px; height: 22px; margin-right: 12px; fill: var(--magenta); }
</style>
</head>
<body>
<main class="canvas">

  <section class="card card--front" aria-label="Card front">
    <div class="brand">
      <span class="brand__dot"></span>
      <span class="brand__text">
        <span class="brand__name">HALDEN CENTER</span>
        <span class="brand__tag">for transgender surgery</span>
      </span>
    </div>
    <span class="edge-tab"></span>

    <div class="doctor">
      <h1 class="doctor__name">Daniel R. Venko, MD</h1>
      <p class="doctor__credentials">Reconstructive Urology for the Transgender Community<br>
      Diplomate, National Council of Renal Medicine with subspecialty<br>
      certification in FPS and Reconstructive Surgery</p>
    </div>

    <address class="address">
      812 Orchard Vale Rd<br>Suite 4<br>Fernmoor, CA 94917
    </address>

    <ul class="contact">
      <li>
        <svg viewBox="0 0 24 24" aria-label="Phone"><path d="M6.6 10.8a15.1 15.1 0 0 0 6.6 6.6l2.2-2.2a1 1 0 0 1 1-.25 11.4 11.4 0 0 0 3.6.57 1 1 0 0 1 1 1V20a1 1 0 0 1-1 1A17 17 0 0 1 3 4a1 1 0 0 1 1-1h3.5a1 1 0 0 1 1 1c0 1.25.2 2.45.57 3.57a1 1 0 0 1-.25 1z"/></svg>
        415-738-2914
      </li>
      <li>
        <svg viewBox="0 0 24 24" aria-label="Fax"><path d="M7 3h10v4H7zM4 8h16a2 2 0 0 1 2 2v6h-4v5H6v-5H2v-6a2 2 0 0 1 2-2zm4 8v3h8v-3zm10-5a1 1 0 1 0 0 2 1 1 0 0 0 0-2z"/></svg>
        415-592-8167
      </li>
    </ul>
  </section>

  <section class="card card--back" aria-label="Card back">
    <div class="brand">
      <span class="brand__dot"></span>
      <span class="brand__text">
        <span class="brand__name">HALDEN CENTER</span>
        <span class="brand__tag">for transgender surgery</span>
      </span>
    </div>
  </section>

</main>
</body>
</html>
```